DJ company new brochure of services offered

I would like to get a new price sheet made for my company services. Currently it's text only. I would like to add pictures next to each service description also like to add general background colors, and just make it look more attractive overall.

Uplighting - File #4 & file #10
Centerpiece pin-spots - File #15
Wedding Cake Spot - file #13 (can you crop out the logo at the bottom)?
Dance Floor Decal File #5
Gobo Monogram - File # 3
market lighting - file #14
ballroom draping - file #7
Video/projections screens: File #13
Indoor safe sparkler effect (not listed on price sheet yet) File #11
Dancing on a cloud - File #9
Co2 Cannons - File #6

Target Market(s)

bride and grooms

Industry/Entity Type

Entertainment

Font styles to use
Serif

Colors

Designer to choose colors to be used in the design.

Requirements
Must have
• my website is www.brightlinkevents.example
• instagram is: @brightlinkevents.example

```html
<!DOCTYPE html>
<html lang="en">
<head>
<meta charset="utf-8">
<title>Brightlink Events – Wedding Reception Price Sheet</title>
<link href="https://fonts.googleapis.com/css2?family=Ubuntu:wght@400;500;700&family=Arimo:ital,wght@0,400;0,700;1,400;1,700&display=swap" rel="stylesheet">
<style>
:root{
  --red:#e8262d;
  --ink:#111;
  --dark-box:#1f1f1f;
  --white:#fff;
  --stage:#e4dcd8;
  --page-bg:#ececec;
  --muted:#444;
}
*{box-sizing:border-box;margin:0;padding:0}
html,body{width:1200px;height:1200px;overflow:hidden;background:var(--page-bg)}
.flyer{position:absolute;left:176px;top:0;width:1022px;height:1445px;transform:scale(.8304);transform-origin:0 0;background:var(--white);font-family:"Arimo",Arial,sans-serif;color:var(--ink);overflow:hidden}
.abs{position:absolute}
.headline{left:0;right:0;top:16px;text-align:center;font-family:"Ubuntu",sans-serif;font-weight:700;font-size:50px;letter-spacing:.3px}
.tagline{left:0;top:85px;width:1022px;height:52px;background:var(--red);color:var(--white);font-size:20px;display:flex;align-items:center;justify-content:center}
.stage{left:0;top:137px;width:1022px;height:1166px;background:linear-gradient(180deg,#d9d0cc 0%,#e9e2de 40%,#efe9e6 70%,#e2dbd8 100%)}
.price{width:156px;height:138px;background:var(--dark-box);color:var(--white);text-align:center;padding-top:34px}
.price .day{font-style:italic;font-weight:700;font-size:17px;letter-spacing:.5px}
.price .amount{font-weight:700;font-size:33px;margin-top:6px}
.price svg{position:absolute;left:2px;bottom:-10px}
.includes-title{left:533px;top:166px;font-weight:700;font-size:22px}
.package{left:533px;top:210px;width:465px;height:322px;background:var(--red);color:var(--white)}
.package ul{position:absolute;left:13px;top:20px;list-style:none;font-size:15.5px;line-height:25.8px}
.package li::before{content:"•";margin-right:9px}
.extra{top:215px;height:63px;border:2px solid var(--white);padding:6px 7px;font-size:11px;line-height:14px}
.extra b{font-family:"Ubuntu",sans-serif;font-size:15px;display:block;letter-spacing:.3px}
.badge{left:818px;top:152px;width:185px;height:175px}
.badge-text{left:818px;top:203px;width:174px;text-align:center;color:var(--white);font-family:"Ubuntu",sans-serif;font-size:16px;line-height:20px;letter-spacing:-.2px}
.heart-photo{left:35px;top:483px;width:452px;height:425px}
.card{width:227px;height:206px;background:var(--white)}
.card .photo{height:138px;position:relative}
.card .cap{position:absolute;left:6px;bottom:2px;color:var(--white);font-family:"Ubuntu",sans-serif;font-weight:700;font-size:13px}
.card .cap.small{font-size:10px}
.card .desc{padding:6px 9px;font-size:11.5px;font-weight:700;line-height:14.5px}
.card .desc i{font-weight:400;font-size:9.5px}
.red{color:var(--red)}
.av{right:26px;top:1250px;font-size:11.5px;font-weight:700}
.offer{left:20px;width:500px;top:1055px;text-align:center;font-family:"Ubuntu",sans-serif;font-weight:500;font-size:37px;line-height:45px}
.offer-cta{left:20px;width:500px;top:1183px;text-align:center;font-family:"Ubuntu",sans-serif;font-weight:700;font-size:23px;color:var(--red)}
.footer{left:0;top:1303px;width:1022px;height:142px;background:var(--white)}
.brand{left:16px;top:62px;display:flex;align-items:center;gap:12px;font-family:"Arimo",sans-serif;font-size:28px;color:var(--red)}
.brand .dot{width:26px;height:26px;border-radius:50%;background:var(--red)}
.contact{left:546px;top:12px;list-style:none;font-size:15px;line-height:20.6px;color:#333}
.contact li::before{content:"•";color:var(--red);margin-right:10px;font-weight:700}
.contact .it{font-style:italic;font-weight:700}
</style>
</head>
<body>
<div class="flyer">
  <h1 class="abs headline">Looking to visually enhance your event ?</h1>
  <div class="abs tagline">We provide a wide-array of lighting and production options to suit the indoor, outdoor, simple or extravagant!</div>

  <div class="abs stage" role="img" aria-label="Soft-focus wedding ballroom with draped backdrop and white dance floor"></div>

  <div class="abs price" style="left:18px;top:204px"><div class="day">SATURDAY</div><div class="amount">$1495</div><svg width="20" height="18"><path d="M2 16 L18 2 L10 6 Z" fill="#e8262d"/></svg></div>
  <div class="abs price" style="left:187px;top:204px"><div class="day">FRI &amp; SUN</div><div class="amount">$1395</div><svg width="20" height="18"><path d="M2 16 L18 2 L10 6 Z" fill="#e8262d"/></svg></div>
  <div class="abs price" style="left:354px;top:204px"><div class="day">MON - TH</div><div class="amount">$1295</div><svg width="20" height="18"><path d="M2 16 L18 2 L10 6 Z" fill="#e8262d"/></svg></div>

  <div class="abs includes-title">THIS PACKAGE INCLUDES:</div>
  <div class="abs package">
    <ul>
      <li>Formally attired &amp; live mixing DJ</li>
      <li>Emcee hosting all announcements</li>
      <li>Powered Speaker Sound System</li>
      <li>Wireless Microphone for toasts, speeches</li>
      <li>In-person consultation to discuss event details</li>
      <li>Online access to planning forms and music database</li>
      <li>Up to 6 hours of continuous entertainment</li>
    </ul>
    <div class="abs extra" style="left:22px;width:209px"><b>CEREMONY MUSIC</b>(includes sound equipment, wireless mic and ceremony music)</div>
    <div class="abs extra" style="left:242px;width:211px"><b>COCKTAIL HOUR MUSIC</b>(includes music in cocktail hour area)</div>
  </div>

  <svg class="abs badge" viewBox="0 0 185 175">
    <path d="M92 170 C45 130 5 100 5 55 C5 25 28 5 55 5 C72 5 86 14 92 28 C98 14 112 5 130 5 C157 5 180 25 180 55 C180 100 140 130 92 170 Z" fill="#e8262d" stroke="#fff" stroke-width="5"/>
    <circle cx="85" cy="125" r="16" fill="none" stroke="#fff" stroke-width="2.5"/>
    <path d="M85 114 V125 L93 131" fill="none" stroke="#fff" stroke-width="2.5"/>
    <circle cx="99" cy="138" r="8" fill="#e8262d" stroke="#fff" stroke-width="2"/>
    <text x="99" y="142" font-size="10" font-family="Arimo,sans-serif" fill="#fff" text-anchor="middle">5</text>
  </svg>
  <div class="abs badge-text">5-HOUR DJ/MC<br>WEDDING RECEPTION<br>PACKAGE</div>

  <svg class="abs heart-photo" viewBox="0 0 452 425" role="img" aria-label="Photo of bride and groom embracing in front of a draped, uplit backdrop">
    <defs><linearGradient id="heartFill" x1="0" y1="0" x2="0" y2="1"><stop offset="0" stop-color="#c99a86"/><stop offset=".55" stop-color="#a77d70"/><stop offset="1" stop-color="#d8c9c4"/></linearGradient></defs>
    <path d="M226 425 C120 330 0 250 0 130 C0 50 60 0 125 0 C175 0 210 30 226 60 C242 30 277 0 327 0 C392 0 452 50 452 130 C452 250 332 330 226 425 Z" fill="url(#heartFill)"/>
  </svg>

  <div class="abs card" style="left:533px;top:527px">
    <div class="photo" role="img" aria-label="Ballroom with warm amber uplighting" style="background:linear-gradient(180deg,#d9a872,#5b3d28)"><span class="cap">UPLIGHTING</span></div>
    <div class="desc">20 fixtures (med-large room) <span class="red">$400</span><br>16 fixtures (med-large room) <span class="red">$350</span><br>12 fixtures (small-large room) <span class="red">$300</span></div>
  </div>
  <div class="abs card" style="left:771px;top:527px">
    <div class="photo" role="img" aria-label="Reception tables with pinspot-lit centerpieces in lavender light" style="background:linear-gradient(180deg,#e4cde8,#9c6fb0)"><span class="cap">PINSPOT LIGHTING</span></div>
    <div class="desc">Wedding cake / Centerpieces /<br>sweetheart table / etc. &nbsp; &nbsp; &nbsp; <span class="red">$30+</span></div>
  </div>
  <div class="abs card" style="left:533px;top:772px">
    <div class="photo" role="img" aria-label="Couple dancing on a seamless white dance floor with decal" style="background:linear-gradient(180deg,#4a3a2c,#a48a6e 60%,#efeae4)"><span class="cap small">SEAMLESS WHITE DANCE FLOOR W/ DECAL</span></div>
    <div class="desc">B&amp;G names appear onto wall or<br>dance floor <span class="red">$250+</span></div>
  </div>
  <div class="abs card" style="left:771px;top:772px">
    <div class="photo" role="img" aria-label="Monogram projected onto a purple-lit dance floor" style="background:linear-gradient(180deg,#8a5a9c,#e0b6e6)"><span class="cap">GOBO MONOGRAM</span></div>
    <div class="desc">B&amp;G names appear onto wall or<br>dance floor <span class="red">$250+</span></div>
  </div>
  <div class="abs card" style="left:533px;top:1021px">
    <div class="photo" role="img" aria-label="Guests dancing in blue and purple lights with CO2 cannon plumes" style="background:linear-gradient(135deg,#3a3f8a,#b58ad0 55%,#f2f0f5)"></div>
    <div class="desc">Dance floor lighting <span class="red">$200+</span><br><i>(depending on style)</i><br>White Dance Floor <span class="red">$1000+</span><br><i>(seamless only)</i></div>
  </div>
  <div class="abs card" style="left:771px;top:1021px">
    <div class="photo" role="img" aria-label="Couple dancing between indoor cold sparkler fountains" style="background:linear-gradient(180deg,#3b2f27,#8f7a66 60%,#e8e2da)"></div>
    <div class="desc" style="padding-top:8px">Indoor safe sparkler effect <span class="red">$not listed</span></div>
  </div>

  <div class="abs av">A/V (screens, projectors, video display) &nbsp;<span class="red">$200+</span></div>

  <div class="abs offer">We offer<br>a wide range of<br>additional services.</div>
  <div class="abs offer-cta">Please contact us for more info &amp; pricing.</div>

  <div class="abs footer">
    <div class="abs brand"><span class="dot"></span>Brightlink Events</div>
    <ul class="abs contact">
      <li>420 Harbor Light Ave. Suite B, Lakeview, CA 90000</li>
      <li>OFFICE LANDLINE: <b>(555) 010-1388</b></li>
      <li>OFFICE MOBILE: <b>(555) 010-3374</b></li>
      <li class="it">hello@brightlinkevents.example</li>
      <li class="it">www.brightlinkevents.example</li>
      <li class="it">@brightlinkevents.example</li>
    </ul>
  </div>
</div>
</body>
</html>
```